Animated custom graphic for hero section of web site home page

I would like a custom graphic that will be used on my new web site home page (see attached image). The graphic must represent revenue growth against projected sales performance. A stylish graph-like image that animates the budget vs. sales results over 12 months could be good. Do some Torvix research for some inspiration.

See the attached example. I want something a bit more stylish. The 2 lines you see on the chart should be animated. The Budget line comes first, then the Actual.

Target Market(s)

CEOs / Founders of B2B SaaS / Tech companies

Industry/Entity Type

SaaS, IT, Tech, Management consulting.

Requirements
Must have
• The custom graphic must represent revenue growth, success etc. Possibly a UI mockup of a CRM dashboard showing quarterly achievement of hitting sales target.The custom graphic must be original, unique and versatile to be used as a custom graphic on ANY web site design with little or no modification. The custom graphic should either use 1 or 2 colors only (black and white)
Nice to have
• ANIMATED - Maybe show a stylish graph with two lines of sales achievement (actual vs. budget) - lines (not bar graph). First the budget line comes up and then the animation shows the actual achieved results) which is better.
Should not have
• No clipart / cartoon style graphics

```html
<!DOCTYPE html>
<html lang="en">
<head>
<meta charset="utf-8">
<title>Achieving Revenue Growth: Performance vs. Projections</title>
<link rel="stylesheet" href="https://fonts.googleapis.com/css2?family=Roboto:wght@400;700&family=Open+Sans:wght@400&display=swap">
<style>
  :root {
    --bg: #35363c;
    --ink: #ffffff;
    --grid: #8d8e93;
    --axis: #c7d3ee;
    --budget: #9a9a9e;
    --actual: #ffffff;
  }
  * { margin: 0; padding: 0; box-sizing: border-box; }
  html, body {
    width: 1200px;
    height: 1200px;
    overflow: hidden;
    background: var(--bg);
  }
  .hero-graphic {
    position: relative;
    width: 1200px;
    height: 1200px;
    background: var(--bg);
  }
  .chart-title {
    position: absolute;
    top: 128px;
    left: 0;
    width: 100%;
    text-align: center;
    color: var(--ink);
    font-family: "Roboto", sans-serif;
    font-weight: 700;
    font-size: 48px;
    line-height: 68px;
    letter-spacing: -0.2px;
  }
  .chart { position: absolute; top: 0; left: 0; }
  .grid-line { stroke: var(--grid); stroke-width: 1.2; }
  .axis-line { stroke: var(--axis); stroke-width: 3; }
  .budget-line {
    fill: none;
    stroke: var(--budget);
    stroke-width: 4;
    stroke-linejoin: round;
    stroke-linecap: round;
  }
  .budget-point { fill: var(--budget); }
  .actual-line {
    fill: none;
    stroke: var(--actual);
    stroke-width: 4;
    stroke-linejoin: round;
    stroke-linecap: round;
  }
  .actual-point { fill: var(--bg); stroke: var(--actual); stroke-width: 3; }
  .month-label {
    fill: var(--ink);
    font-family: "Open Sans", sans-serif;
    font-size: 24px;
    text-anchor: middle;
  }
  .legend-swatch { stroke-width: 5; }
  .legend-swatch--budget { stroke: var(--budget); }
  .legend-swatch--actual { stroke: var(--actual); }
  .legend-label {
    fill: var(--ink);
    font-family: "Open Sans", sans-serif;
    font-size: 26px;
  }
</style>
</head>
<body>
<main class="hero-graphic">
  <h1 class="chart-title">Achieving Revenue Growth:<br>Performance vs. Projections</h1>

  <svg class="chart" width="1200" height="1200" viewBox="0 0 1200 1200" aria-label="Line chart of budget and actual revenue over twelve months">
    <g class="grid">
      <line class="grid-line" x1="101" y1="446" x2="1118" y2="446"/>
      <line class="grid-line" x1="101" y1="549" x2="1118" y2="549"/>
      <line class="grid-line" x1="101" y1="652" x2="1118" y2="652"/>
      <line class="grid-line" x1="101" y1="754" x2="1118" y2="754"/>
      <line class="grid-line" x1="101" y1="857" x2="1118" y2="857"/>
    </g>

    <line class="axis-line" x1="101" y1="917" x2="1121" y2="917"/>

    <g class="budget-series">
      <polyline class="budget-line" points="134,880 220,848 305,816 389,784 474,752 559,720 644,688 728,656 814,624 899,592 983,560 1068,528"/>
      <circle class="budget-point" cx="134" cy="880" r="6"/>
      <circle class="budget-point" cx="220" cy="848" r="6"/>
      <circle class="budget-point" cx="305" cy="816" r="6"/>
      <circle class="budget-point" cx="389" cy="784" r="6"/>
      <circle class="budget-point" cx="474" cy="752" r="6"/>
      <circle class="budget-point" cx="559" cy="720" r="6"/>
      <circle class="budget-point" cx="644" cy="688" r="6"/>
      <circle class="budget-point" cx="728" cy="656" r="6"/>
      <circle class="budget-point" cx="814" cy="624" r="6"/>
      <circle class="budget-point" cx="899" cy="592" r="6"/>
      <circle class="budget-point" cx="983" cy="560" r="6"/>
      <circle class="budget-point" cx="1068" cy="528" r="6"/>
    </g>

    <g class="actual-series">
      <polyline class="actual-line" points="134,895 220,872 305,846 389,802 474,762 559,732 644,678 728,636 814,588 899,548 983,498 1068,458"/>
      <circle class="actual-point" cx="134" cy="895" r="7"/>
      <circle class="actual-point" cx="220" cy="872" r="7"/>
      <circle class="actual-point" cx="305" cy="846" r="7"/>
      <circle class="actual-point" cx="389" cy="802" r="7"/>
      <circle class="actual-point" cx="474" cy="762" r="7"/>
      <circle class="actual-point" cx="559" cy="732" r="7"/>
      <circle class="actual-point" cx="644" cy="678" r="7"/>
      <circle class="actual-point" cx="728" cy="636" r="7"/>
      <circle class="actual-point" cx="814" cy="588" r="7"/>
      <circle class="actual-point" cx="899" cy="548" r="7"/>
      <circle class="actual-point" cx="983" cy="498" r="7"/>
      <circle class="actual-point" cx="1068" cy="458" r="7"/>
    </g>

    <g class="month-labels">
      <text class="month-label" x="138" y="975">Jan</text>
      <text class="month-label" x="226" y="975">Feb</text>
      <text class="month-label" x="305" y="975">Mar</text>
      <text class="month-label" x="392" y="975">Apr</text>
      <text class="month-label" x="485" y="975">May</text>
      <text class="month-label" x="564" y="975">Jun</text>
      <text class="month-label" x="647" y="975">Jul</text>
      <text class="month-label" x="731" y="975">Aug</text>
      <text class="month-label" x="821" y="975">Sept</text>
      <text class="month-label" x="906" y="975">Oct</text>
      <text class="month-label" x="991" y="975">Nov</text>
      <text class="month-label" x="1080" y="975">Dec</text>
    </g>

    <g class="legend">
      <line class="legend-swatch legend-swatch--budget" x1="372" y1="1071" x2="427" y2="1071"/>
      <text class="legend-label" x="445" y="1080">Budget</text>
      <line class="legend-swatch legend-swatch--actual" x1="640" y1="1071" x2="695" y2="1071"/>
      <text class="legend-label" x="713" y="1080">Actual</text>
    </g>
  </svg>
</main>
</body>
</html>
```